Tall Fern Software

We are a software company selling endpoint visibility, access and security technology to enterprise-level IT departments.

Our technology helps organizations gain comprehensive visibility into and control over devices accessing their corporate network so they can quickly identify and address suspicious activity on the network that could lead to potential threats like data breaches.

This technology can cost organizations upwards of $1M - depending on the size of the organization. Our primary clients are Pinnacle 2,000 companies.

We want a professional, polished business card to represent our new brand.

Info fields to include on the card:
Name
Job Title
Office Phone #
Cell Phone #
Email address
Address: 4217 Westbrook Ridge Blvd., Ste. 2600, Fairhaven, WI 55918
Website address: www.tallfernsoftware.example
Tagline: See every device. Secure the network.

Logo files and color specs document are attached. Would like color scheme to coordinate with the logo.

Also looking at stationary/envelope designs in conjunction with the business card designs. Received very few designs that included the stationary.

```html
<!DOCTYPE html>
<html lang="en">
<head>
<meta charset="utf-8">
<title>Tall Fern Software – Business Card</title>
<link href="https://fonts.googleapis.com/css2?family=Open+Sans:wght@400;600;700&display=swap" rel="stylesheet">
<style>
  :root {
    --page-bg: #e9e7e4;
    --card-bg: #ffffff;
    --card-edge: #cfcfcf;
    --brand-red: #8c1010;
    --band-red: #800000;
    --ink: #2f2f2f;
    --rule: #9a9a9a;
    --band-text: #ffffff;
  }
  * { box-sizing: border-box; margin: 0; padding: 0; }
  html, body {
    width: 1200px; height: 587px; overflow: hidden;
    background: var(--page-bg);
    font-family: "Open Sans", Arial, sans-serif;
    color: var(--ink);
  }
  .canvas { position: relative; width: 1200px; height: 587px; }
  .card {
    position: absolute; top: 123px; width: 555px; height: 341px;
    background: var(--card-bg);
    border: 1px solid var(--card-edge);
    box-shadow: 0 2px 6px rgba(0,0,0,.18);
    overflow: hidden;
  }
  .card--front { left: 32px; }
  .card--back { left: 613px; }

  .brand { display: flex; align-items: center; gap: 12px; }
  .brand__dot { width: 22px; height: 22px; border-radius: 50%; background: var(--brand-red); flex: none; }
  .brand__name { font-weight: 700; color: var(--brand-red); font-size: 28px; letter-spacing: .5px; line-height: 1; }

  .card--front .brand { position: absolute; left: 30px; top: 62px; }

  .person { position: absolute; left: 28px; top: 155px; }
  .person__name { font-size: 18px; font-weight: 400; line-height: 1.2; }
  .person__title { font-size: 12.5px; color: var(--brand-red); margin-top: 1px; }

  .contacts { position: absolute; left: 28px; top: 203px; list-style: none; }
  .contacts li { display: flex; align-items: center; gap: 8px; font-size: 12.5px; height: 20px; }
  .contacts svg { width: 10px; height: 10px; fill: var(--brand-red); flex: none; }

  .address-band {
    position: absolute; left: 0; right: 0; bottom: 0; height: 41px;
    background: var(--band-red); color: var(--band-text);
    display: flex; align-items: center; justify-content: center; gap: 8px;
    font-size: 13px;
  }
  .address-band svg { width: 9px; height: 11px; fill: var(--band-text); }

  .card--back .brand { position: absolute; left: 0; right: 0; top: 130px; justify-content: center; }
  .tagline-rule { position: absolute; left: 127px; width: 299px; top: 209px; border-top: 1px solid var(--rule); }
  .tagline { position: absolute; left: 0; right: 0; top: 214px; text-align: center; font-size: 17px; color: #1f1f1f; }
</style>
</head>
<body>
<div class="canvas">

  <section class="card card--front" aria-label="Business card front">
    <div class="brand">
      <span class="brand__dot"></span>
      <span class="brand__name">Tall Fern Software</span>
    </div>

    <div class="person">
      <p class="person__name">Marisa Kellwood</p>
      <p class="person__title">Vice President of Marketing</p>
    </div>

    <ul class="contacts">
      <li>
        <svg viewBox="0 0 10 10" aria-hidden="true"><path d="M2 0.5l1.8 2-1 1.2c.6 1.3 1.5 2.2 2.6 2.7l1.1-1 2 1.8-1.2 1.8C4.5 8.7 1.2 5.4 0.5 1.8z"/></svg>
        <span>+1 555.014.2738</span>
      </li>
      <li>
        <svg viewBox="0 0 10 10" aria-hidden="true"><path d="M3 0h4a1 1 0 0 1 1 1v8a1 1 0 0 1-1 1H3a1 1 0 0 1-1-1V1a1 1 0 0 1 1-1zm0 1.5v6h4v-6zm2 6.8a.5.5 0 1 0 0 .1z"/></svg>
        <span>+1 555.019.6042</span>
      </li>
      <li>
        <svg viewBox="0 0 10 10" aria-hidden="true"><path d="M0 2h10v.6L5 5.6 0 2.6zm0 1.7l5 3 5-3V8H0z"/></svg>
        <span>mkellwood@tallfernsoftware.example</span>
      </li>
      <li>
        <svg viewBox="0 0 10 10" aria-hidden="true"><path d="M5 0a5 5 0 1 0 0 10A5 5 0 0 0 5 0zm-.6 1.2C3.8 2 3.5 3.2 3.4 4.4H1.2a3.9 3.9 0 0 1 3.2-3.2zm1.2 0a3.9 3.9 0 0 1 3.2 3.2H6.6C6.5 3.2 6.2 2 5.6 1.2zM4.5 4.4c.1-1.1.3-2 .5-2.7.2.7.4 1.6.5 2.7zm-3.3 1.2h2.2c.1 1.2.4 2.4 1 3.2a3.9 3.9 0 0 1-3.2-3.2zm3.3 0h1c-.1 1.1-.3 2-.5 2.7-.2-.7-.4-1.6-.5-2.7zm2.1 0h2.2a3.9 3.9 0 0 1-3.2 3.2c.6-.8.9-2 1-3.2z"/></svg>
        <span>www.tallfernsoftware.example</span>
      </li>
    </ul>

    <div class="address-band">
      <svg viewBox="0 0 9 11" aria-hidden="true"><path d="M4.5 0A4.5 4.5 0 0 0 0 4.5C0 7.5 4.5 11 4.5 11S9 7.5 9 4.5A4.5 4.5 0 0 0 4.5 0zm0 6.2a1.7 1.7 0 1 1 0-3.4 1.7 1.7 0 0 1 0 3.4z"/></svg>
      <span>4217 Westbrook Ridge Blvd., Ste. 2600, Fairhaven, WI 55918, USA</span>
    </div>
  </section>

  <section class="card card--back" aria-label="Business card back">
    <div class="brand">
      <span class="brand__dot"></span>
      <span class="brand__name">Tall Fern Software</span>
    </div>
    <div class="tagline-rule"></div>
    <p class="tagline">See every device. Secure the network.</p>
  </section>

</div>
</body>
</html>
```